Alcohol/Drug addiction treatment center and detox facility needs a billboard.

We are a new treatment center in Auburn, IN (2020), specializing in helping folks who are struggling with alcohol/drug addiction. We offer medical detox, inpatient, and outpatient care in a beautiful, safe, and stable environment, where patients will detox comfortably and then learn the coping skills necessary to lead a successful, sober life. The ad should reach people on a personal/emotional level - addicts who are overwhelmed as well as their families - reminding them that the tentacles of addiction are far-reaching; further, it should convey that you are not alone, we are committed to helping you learn how to lead a successful life, and we are here 24/7/365.
Updates

Here are some slogans that are popular in the treatment industry right now: -Your baby’s life shouldn’t begin with 1-833-HEALS-NOW (Maybe use our phone number as the last word) -Treatment Changes Everything. -Brookmere turns fear into Hope. -Pain killers are easy to get into hard to escape -It only takes a little to lose a lot. -Alcohol, Herion, Pills it all kills. -Loved one hooked on Herion? Brookmere ect. -Drive Hammered get nailed -Recovery is real -Brookmere turns fear into hope.

Target Market(s)

People struggling with addiction and their families.

Industry/Entity Type

Addiction Treatment centers

Colors

Designer to choose colors to be used in the design.

Requirements
Must have
• Brookmere Treatment; 833-HEALS-NOW; www.brookmeretreatment-example.com
Nice to have
• Catchy slogan - Examples: 1. Your baby’s life shouldn’t begin with 1-833-HEALS-Now (we could use our phone number for the last word) 2. Treatment Changes Everything. 3. It only takes a little to lose a lot. 4. Alcohol, Heroin, Pills it all kills. 5. Loved one hooked on Heroin? Brookmere can help. 6. Drive Hammered get nailed 7. Recovery is real 8. Brookmere turns fear into hope. 9. Pain killers are easy to get into hard to escape

```html
<!DOCTYPE html>
<html lang="en">
<head>
<meta charset="utf-8">
<title>Brookmere Treatment – Billboard</title>
<link href="https://fonts.googleapis.com/css2?family=Barlow+Semi+Condensed:wght@500;600&family=Montserrat:wght@500&display=swap" rel="stylesheet">
<style>
  :root {
    --page: #e9ebef;
    --navy: #0c1a36;
    --navy-panel: #0e1d3d;
    --cyan: #29b8ea;
    --white: #ffffff;
    --ring: #2a4f7a;
    --badge-ink: #2b2f8f;
  }
  * { margin: 0; padding: 0; box-sizing: border-box; }
  html, body {
    width: 1200px; height: 442px; overflow: hidden;
    background: var(--page);
  }
  .billboard {
    position: absolute; left: 20px; top: 52px;
    width: 1160px; height: 337px;
    background: var(--navy);
    overflow: hidden;
  }
  .billboard-art { position: absolute; inset: 0; }
  .chevrons {
    position: absolute; left: 792px; top: 30px;
    color: var(--white);
    font: 500 11px/1 "Barlow Semi Condensed", sans-serif;
    letter-spacing: 3px;
  }
  .services {
    position: absolute; left: 582px; top: 80px;
    list-style: none;
  }
  .service {
    display: flex; align-items: center; gap: 6px;
    color: var(--cyan);
    font: 600 52px/64px "Barlow Semi Condensed", sans-serif;
    letter-spacing: -0.3px;
  }
  .service svg { width: 42px; height: 42px; flex: none; }
  .service-note {
    position: absolute; left: 584px; top: 210px;
    width: 308px;
    color: var(--white);
    font: 500 13.5px/18.5px "Barlow Semi Condensed", sans-serif;
  }
  .contact {
    position: absolute; left: 584px; top: 272px;
    font-family: "Barlow Semi Condensed", sans-serif;
  }
  .contact-phone {
    color: var(--cyan);
    font-weight: 600; font-size: 24px; line-height: 28px;
    letter-spacing: 0.5px;
  }
  .contact-web {
    color: var(--white);
    font-weight: 500; font-size: 14px; line-height: 18px;
  }
  .brand {
    position: absolute; left: 912px; top: 96px; width: 224px;
    display: flex; flex-direction: column; align-items: center;
  }
  .brand-mark {
    width: 90px; height: 90px; border-radius: 50%;
    background: var(--cyan); margin-bottom: 22px;
  }
  .brand-name {
    color: var(--white); text-align: center;
    font: 500 24px/1.15 "Montserrat", sans-serif;
    letter-spacing: 1.5px;
  }
</style>
</head>
<body>
  <section class="billboard">
    <svg class="billboard-art" width="1160" height="337" viewBox="0 0 1160 337">
      <defs>
        <radialGradient id="photoTone" cx="45%" cy="55%" r="65%">
          <stop offset="0" stop-color="#a9b4bd"/>
          <stop offset="0.45" stop-color="#5d6b78"/>
          <stop offset="1" stop-color="#1c2128"/>
        </radialGradient>
        <linearGradient id="ringGlow" x1="0" y1="0" x2="1" y2="1">
          <stop offset="0" stop-color="#2ab9ea"/>
          <stop offset="1" stop-color="#5f9d8e"/>
        </linearGradient>
        <clipPath id="photoClip"><circle cx="280" cy="168" r="200"/></clipPath>
      </defs>

      <path d="M515 0 H1160 V337 H575 C640 260 650 90 515 0 Z" fill="var(--navy-panel)"/>
      <path d="M1090 337 C1130 300 1150 260 1160 230 V337 Z" fill="#163f4f" opacity="0.6"/>

      <g fill="none" stroke="var(--ring)" stroke-width="0.8" opacity="0.7">
        <circle cx="280" cy="168" r="218"/>
        <circle cx="280" cy="168" r="232"/>
        <circle cx="280" cy="168" r="246"/>
        <circle cx="280" cy="168" r="260"/>
      </g>

      <circle cx="280" cy="168" r="206" fill="none" stroke="url(#ringGlow)" stroke-width="10" opacity="0.85"/>

      <g role="img" aria-label="Close-up of a hand holding a burning cigarette surrounded by drifting smoke">
        <rect x="60" y="-40" width="440" height="420" fill="url(#photoTone)" clip-path="url(#photoClip)"/>
      </g>

      <path d="M57 168 A223 223 0 0 1 175 -28" fill="none" stroke="var(--cyan)" stroke-width="22"/>
      <rect x="472" y="170" width="26" height="30" fill="var(--cyan)"/>

      <g class="badge-247">
        <circle cx="460" cy="250" r="64" fill="var(--white)"/>
        <circle cx="460" cy="250" r="30" fill="none" stroke="var(--badge-ink)" stroke-width="1.6"/>
        <path d="M420 240 A42 42 0 0 1 488 218" fill="none" stroke="var(--badge-ink)" stroke-width="1.6"/>
        <path d="M488 218 l-2 -12 M488 218 l-12 2" stroke="var(--badge-ink)" stroke-width="1.6" fill="none"/>
        <path d="M500 262 A42 42 0 0 1 432 282" fill="none" stroke="var(--badge-ink)" stroke-width="1.6"/>
        <path d="M432 282 l2 12 M432 282 l12 -2" stroke="var(--badge-ink)" stroke-width="1.6" fill="none"/>
        <text x="460" y="258" text-anchor="middle" fill="var(--badge-ink)"
              font-family="Barlow Semi Condensed, sans-serif" font-weight="500" font-size="24">24/7</text>
      </g>

      <g fill="var(--white)">
        <circle cx="896" cy="285" r="1.3"/><circle cx="907" cy="285" r="1.3"/><circle cx="918" cy="285" r="1.3"/>
        <circle cx="896" cy="297" r="1.3"/><circle cx="907" cy="297" r="1.3"/><circle cx="918" cy="297" r="1.3"/>
        <circle cx="896" cy="309" r="1.3"/><circle cx="907" cy="309" r="1.3"/><circle cx="918" cy="309" r="1.3"/>
      </g>
    </svg>

    <div class="chevrons">&gt;&gt;&gt;&gt;</div>

    <ul class="services">
      <li class="service">
        <svg viewBox="0 0 44 44"><circle cx="21" cy="23" r="18" fill="none" stroke="var(--cyan)" stroke-width="4"/><path d="M12 22 l8 9 L40 6" fill="none" stroke="var(--cyan)" stroke-width="5" stroke-linecap="round" stroke-linejoin="round"/></svg>
        Medical Detox
      </li>
      <li class="service">
        <svg viewBox="0 0 44 44"><circle cx="21" cy="23" r="18" fill="none" stroke="var(--cyan)" stroke-width="4"/><path d="M12 22 l8 9 L40 6" fill="none" stroke="var(--cyan)" stroke-width="5" stroke-linecap="round" stroke-linejoin="round"/></svg>
        Inpatient
      </li>
    </ul>

    <p class="service-note">where patients will detox comfortably and then learn the coping skills necessary to lead a successful, sober life.</p>

    <div class="contact">
      <p class="contact-phone">833-HEALS-NOW</p>
      <p class="contact-web">www.brookmeretreatment-example.com</p>
    </div>

    <div class="brand">
      <div class="brand-mark"></div>
      <p class="brand-name">BROOKMERE<br>TREATMENT</p>
    </div>
  </section>
</body>
</html>
```